4 Business Card templates for printing site

I want 4 business card templates (including a front and a back). You should provide a variety of designs covering a cross section of industries. It is fine if this is taken from variations on designs of previous work that you have produced.

**All the designs can be provided in one file**

The templates will be used for a website I am building which is targeted at servicing printing requirements for micro businesses (small business with less than 10 people). The first product to be launched is business cards. I will require ~500 designs so this initial phase is partly to identify potential designers with the capability to produce a broad range of designs to populate the site.

For this project 4 templates are required in total.
I want 2 generic designs - designs that are not industry specific (just simple classic modern templates), one that would have room for a logo to be added and one that works well as a design without a logo.

The other 4 designs can be across any industry. These will be for business without logos that still want to have a flavour of what they do represented by the card. These can include illustrations or photos.

Below is a list of industries which the templates will cover: Accountancy, Finance,Advertising, PR, Animal & Pet Care, Architecture, Builders, Childcare, cleaning, Driving Instructors, Education & Training, Electrician,Fashion, Florist / gardening,Hairdresser, Legal, Medical & Dental, Music & DJ, Painter, photographer, Plumber, Real Estate & Property, Salons, Spas, Wellbeing & Beauty, Sports & Fitness, Trademen - carpenter, handyman, Wedding Event & Party Planing.

For inspiration below are some sites where examples of templates can be seen:

Graphic / illustrative templates:
http://uk.pellora.com/design-templates/business-cards/
and example of industry specific such as a plumber:
http://uk.pellora.com/design-templates/business-cards/?search=industry:%22DIY%20%26%20Tradesmen%22&advsearch=1&filters=1

Example of card design treatment with photo front and back
http://www.quorvix.com/product/582731/details.htm

and of course the biggest online printer (although design quality is not very high).
http://www.brellmont.co.uk/gallery/QZRTUUVWXYZABCD=/premium-business-cards.aspx?xnav=HowToDesign

For designers that submit work that does not win, I will pay £20 for specific templates that I want to use on the site.

For the winning designs I will require SVG files.
Updates

Project Deadline Extended
Reason: Only 4 entries received. As this is the first time using this service I was expecting greater range.

Project Deadline Extended
Reason: Hoping to have 10 designer entries.

Target Market(s)

Micro businesses (small business with less than 10 people). Often self employed people.

Industry/Entity Type

Printing

Requirements
Nice to have
• I want to see well balanced designs, which have good use of space, font, colour and graphics.
Should not have
• I do not want to see poor quality "clip art" style designs!

```html
<!DOCTYPE html>
<html lang="en">
<head>
<meta charset="utf-8">
<title>Tarnvale Business Card – Front and Back</title>
<link rel="stylesheet" href="https://fonts.googleapis.com/css2?family=Montserrat:wght@800&family=Quicksand:wght@300;400;600&display=swap">
<style>
  :root {
    --page-edge: #c6c6c6;
    --page-mid: #ffffff;
    --card-base: #7a7a7a;
    --card-deep: #525252;
    --stripe: #b8b8b8;
    --stripe-shadow: #2a2a2a;
    --ink-dark: #111111;
    --ink-light: #f4f4f4;
    --label-tint: #9ea7b1;
    --rule-light: #e6e6e6;
  }
  * { box-sizing: border-box; margin: 0; padding: 0; }
  html, body { width: 1200px; height: 1200px; overflow: hidden; }
  body {
    position: relative;
    background: linear-gradient(to bottom, var(--page-edge) 0%, var(--page-mid) 50%, var(--page-edge) 100%);
    font-family: "Quicksand", "Helvetica Neue", Arial, sans-serif;
  }
  .card {
    position: absolute;
    left: 222px;
    width: 738px;
    height: 476px;
    border-radius: 22px;
    overflow: hidden;
    background:
      radial-gradient(ellipse 75% 85% at 100% 0%, var(--card-deep) 0%, rgba(82,82,82,0) 70%),
      var(--card-base);
  }
  .card--front { top: 77px; }
  .card--back  { top: 634px; }
  .card__stripes { position: absolute; inset: 0; width: 100%; height: 100%; }

  .brand {
    position: absolute;
    font-family: "Montserrat", Arial, sans-serif;
    font-weight: 800;
    color: var(--ink-dark);
    letter-spacing: 0.01em;
    white-space: nowrap;
  }
  .card--front .brand {
    left: 0; right: 0; top: 238px;
    text-align: center;
    font-size: 56px;
    line-height: 1;
    transform: translateY(-50%);
  }
  .card--back .brand {
    right: 30px; top: 40px;
    font-size: 27px;
    line-height: 1;
  }

  .holder__name {
    position: absolute;
    left: 88px; top: 36px;
    font-weight: 300;
    font-variant: small-caps;
    font-size: 44px;
    line-height: 1;
    letter-spacing: 0.04em;
    color: var(--ink-light);
  }
  .rule {
    position: absolute;
    height: 2px;
    background: linear-gradient(to right, rgba(230,230,230,0) 0%, var(--rule-light) 20%, var(--rule-light) 80%, rgba(230,230,230,0) 100%);
    box-shadow: 0 1px 1px rgba(0,0,0,0.35);
  }
  .rule--name { left: 16px; top: 86px; width: 406px; }
  .rule--web  { left: 16px; top: 428px; width: 416px; }
  .holder__role {
    position: absolute;
    left: 135px; top: 96px;
    font-style: italic;
    font-size: 19px;
    letter-spacing: 0.14em;
    color: var(--ink-light);
    transform: skewX(-10deg);
  }

  .contact { position: absolute; left: 18px; top: 215px; list-style: none; }
  .contact__item { margin-bottom: 4px; }
  .contact__label {
    display: block;
    font-weight: 600;
    font-size: 17px;
    line-height: 20px;
    color: var(--label-tint);
  }
  .contact__value {
    display: block;
    font-weight: 400;
    font-size: 21px;
    line-height: 28px;
    color: var(--ink-light);
  }
  .web {
    position: absolute;
    left: 44px; top: 436px;
    font-size: 25px;
    letter-spacing: 0.04em;
    color: var(--ink-light);
  }
</style>
</head>
<body>

  <section class="card card--front" aria-label="Card front">
    <svg class="card__stripes" viewBox="0 0 615 397" preserveAspectRatio="none" aria-hidden="true">
      <defs>
        <filter id="stripe-shadow-front" x="-20%" y="-20%" width="140%" height="140%">
          <feDropShadow dx="6" dy="5" stdDeviation="5" flood-color="#2a2a2a" flood-opacity="0.55"/>
        </filter>
      </defs>
      <g fill="var(--stripe)" filter="url(#stripe-shadow-front)">
        <polygon points="342,397 388,397 785,0 739,0"/>
        <polygon points="455,397 501,397 898,0 852,0"/>
        <polygon points="570,397 616,397 1013,0 967,0"/>
      </g>
    </svg>
    <div class="brand">TARNVALE</div>
  </section>

  <section class="card card--back" aria-label="Card back">
    <svg class="card__stripes" viewBox="0 0 615 397" preserveAspectRatio="none" aria-hidden="true">
      <defs>
        <filter id="stripe-shadow-back" x="-20%" y="-20%" width="140%" height="140%">
          <feDropShadow dx="6" dy="5" stdDeviation="5" flood-color="#2a2a2a" flood-opacity="0.55"/>
        </filter>
      </defs>
      <g fill="var(--stripe)" filter="url(#stripe-shadow-back)">
        <polygon points="342,397 388,397 785,0 739,0"/>
        <polygon points="455,397 501,397 898,0 852,0"/>
        <polygon points="570,397 616,397 1013,0 967,0"/>
      </g>
    </svg>

    <h1 class="holder__name">Alex Marlow</h1>
    <div class="rule rule--name"></div>
    <p class="holder__role">CONSULTANT</p>

    <div class="brand">TARNVALE</div>

    <ul class="contact">
      <li class="contact__item"><span class="contact__label">p.</span><span class="contact__value">+44 (0) 1632 960418</span></li>
      <li class="contact__item"><span class="contact__label">m.</span><span class="contact__value">+44 (0) 7700 900123</span></li>
      <li class="contact__item"><span class="contact__label">e.</span><span class="contact__value">amarlow@tarnvale.com</span></li>
    </ul>

    <div class="rule rule--web"></div>
    <p class="web">www.tarnvale.com</p>
  </section>

</body>
</html>
```